Maison Vurel

menu design, menu change,
will send hand written rough draft soon
Updates

Project Deadline Extended
Reason: Got off to a slow start. Things are progressing now. Thank you.

Target Market(s)

18-60 yr olds, blue collar & professionals, middle class, median income, families,upscale - casual- steakhouse concept

Industry/Entity Type

Restaurant

Colors
f68d4c
f37122
f78f20
faa54b
ffc214
fece3e
fbee3e
fbed22
333333

Requirements
Must have
• Front cover, back cover. 2 inside views
Nice to have
• 8 x 14 page size

```html
<!DOCTYPE html>
<html lang="en">
<head>
<meta charset="utf-8">
<title>Maison Vurel Menu – Inside Spread</title>
<link href="https://fonts.googleapis.com/css2?family=Rye&family=Open+Sans:wght@400;700&display=swap" rel="stylesheet">
<style>
:root{
  --cream:#fdf1e3;
  --red:#ec2227;
  --orange:#f78f20;
  --panel-light:#fece7e;
  --panel-mid:#faa54b;
  --yellow:#fbee3e;
  --title-yellow:#ffe21a;
  --ink:#1e1e1e;
  --ink-soft:#333333;
  --white:#ffffff;
}
*{margin:0;padding:0;box-sizing:border-box}
html,body{width:1200px;height:1061px;overflow:hidden;background:var(--cream)}
.menu{position:relative;width:1200px;height:1061px;font-family:"Open Sans",sans-serif;color:var(--ink)}
.page{position:absolute;top:53px;height:955px;background:var(--red);box-shadow:3px 4px 6px rgba(0,0,0,.25)}
.page--left{left:55px;width:545px}
.page--right{left:602px;width:545px}
.field{position:absolute;background:linear-gradient(160deg,#fdd99a 0%,var(--panel-light) 45%,var(--panel-mid) 100%)}
.photo{position:absolute;z-index:1;border-radius:50%;background:radial-gradient(circle at 45% 45%,#f6b48a,#c9473f 55%,#f4f1ea 72%,#ffffff 100%)}
.photo--greens{background:radial-gradient(circle,#3f6b2a,#c8593a 45%,#f5f5f5 62%,#ffffff 100%)}
.photo--fries{background:radial-gradient(circle,#f6c24a,#e2843a 45%,#f5f5f5 62%,#ffffff 100%)}
.section-title{position:absolute;z-index:2;font-family:"Rye",serif;font-weight:400;color:var(--title-yellow);font-size:50px;line-height:1;white-space:nowrap;transform:scaleX(.53);transform-origin:left top}
.section-title--red{color:var(--red)}
.note-tab{position:absolute;z-index:2;left:100px;top:198px;width:287px;height:35px;background:#111;border-radius:0 0 14px 14px;color:var(--white);font-size:11.5px;font-weight:700;padding:10px 0 0 25px}
.item{position:absolute;width:260px}
.item__name{font-weight:700;font-size:13.5px;line-height:14px;text-transform:uppercase}
.item__desc{font-size:10px;line-height:10.5px;color:var(--ink-soft)}
.price{position:absolute;font-weight:700;font-size:16px}
.sides{position:absolute;left:107px;top:640px;width:440px;height:353px;background:var(--red);border-radius:16px 16px 0 0}
.band{position:absolute;left:0;width:440px;background:var(--yellow)}
.sides__list{position:absolute;left:25px;top:102px;color:var(--white);font-size:14px;line-height:18.3px}
.sides__prices{position:absolute;left:366px;top:102px;color:var(--white);font-size:16px;font-weight:700;line-height:18.3px}
.potato-list{position:absolute;left:0;width:440px;top:290px;text-align:center;color:var(--white);font-size:14px;line-height:19px}
.potato-list span{padding:0 8px;border-left:2px solid var(--white)}
.potato-list span:first-child{border-left:none}
</style>
</head>
<body>
<div class="menu">

  <!-- left page -->
  <div class="page page--left"></div>
  <div class="field" style="left:68px;top:68px;width:517px;height:60px"></div>
  <div class="field" style="left:68px;top:198px;width:517px;height:795px"></div>
  <div class="photo" role="img" aria-label="Plate of sliced sashimi and seafood" style="left:395px;top:82px;width:190px;height:140px;transform:rotate(20deg)"></div>
  <h2 class="section-title" style="left:112px;top:142px">Chicken or Seafood</h2>
  <div class="note-tab">served with choice of Potato + Hot Bread</div>

  <div class="item" style="left:132px;top:249px;width:290px"><div class="item__name">Charbroiled Chicken Breast</div><div class="item__desc">10oz Flame broiled Breast</div></div>
  <div class="price" style="left:474px;top:246px">14.99</div>
  <div class="item" style="left:132px;top:288px"><div class="item__name">North Atlante Salmon</div><div class="item__desc">charbroiled Fillet 8oz</div></div>
  <div class="price" style="left:474px;top:285px">19.99</div>
  <div class="item" style="left:132px;top:327px;width:260px"><div class="item__name">Chicken Fried Chicken Breast</div><div class="item__desc">10oz hand breaded Breast, fried, served with<br>corn on the cab, mashed potatoes + country gravy</div></div>
  <div class="price" style="left:474px;top:324px">14.99</div>
  <div class="item" style="left:132px;top:377px"><div class="item__name">English Style Cod</div><div class="item__desc">House battered Icelandic Cod Lions</div></div>
  <div class="price" style="left:474px;top:374px">17.99</div>
  <div class="item" style="left:132px;top:416px;width:290px"><div class="item__name">Hand Breaded Chicken Strips</div><div class="item__desc">Cut + Breaded per order</div></div>
  <div class="price" style="left:474px;top:413px">9.99</div>
  <div class="item" style="left:132px;top:455px"><div class="item__name">Deep Fried Gulf Shrimp</div><div class="item__desc">6 Jumbo shrimp</div></div>
  <div class="price" style="left:474px;top:452px">17.99</div>
  <div class="item" style="left:132px;top:494px;width:260px"><div class="item__name">Chicken Ka-Bob</div><div class="item__desc">10oz Charbroiled Breast, Skewered with bell peppers,<br>onionsm mushrooms, tomatoes, pineapple,<br>and drizzeled with light Italian marinade</div></div>
  <div class="price" style="left:474px;top:491px">19.99</div>
  <div class="item" style="left:132px;top:554px;width:260px"><div class="item__name">Mahi Mahi</div><div class="item__desc">9oz charbroiled served under a shrimp + mushroom<br>white sauce on a bed of Steamed garden vegetables</div></div>
  <div class="price" style="left:474px;top:551px">19.99</div>
  <div class="item" style="left:132px;top:603px"><div class="item__name">Country Fried Catfish</div><div class="item__desc">Catfish Fillets, hand breaded + deep fried</div></div>
  <div class="price" style="left:474px;top:600px">12.99</div>

  <div class="sides">
    <div class="band" style="top:38px;height:54px"></div>
    <div class="photo photo--greens" role="img" aria-label="Plate of sautéed spinach and carrots" style="left:250px;top:18px;width:130px;height:90px"></div>
    <h2 class="section-title section-title--red" style="left:25px;top:42px">Sides</h2>
    <div class="sides__list">steamed Garden Vegetables<br>Twice Baked Potato<br>Loaded Baked + Mashed potato<br>Grilled Asparages<br>House or Casar Salad<br>* If in place of potato, Add</div>
    <div class="sides__prices">4.99<br>4.99<br>4.99<br>4.99<br>4.99<br>2.99</div>
    <div class="band" style="top:220px;height:55px"></div>
    <div class="photo photo--fries" role="img" aria-label="Plate of french fries with garnish" style="left:262px;top:206px;width:118px;height:82px"></div>
    <h2 class="section-title section-title--red" style="left:25px;top:225px">Potato choices</h2>
    <div class="potato-list">
      <div><span>Baked</span><span>Mashed</span><span>American Fries</span></div>
      <div><span>German Fries</span><span>French Fries</span><span>Onion Rings</span></div>
    </div>
  </div>

  <!-- right page -->
  <div class="page page--right"></div>
  <div class="field" style="left:615px;top:68px;width:517px;height:60px"></div>
  <div class="field" style="left:615px;top:200px;width:517px;height:412px"></div>
  <div class="field" style="left:615px;top:682px;width:517px;height:311px"></div>
  <div class="photo" role="img" aria-label="Plated dessert with sauce drizzle" style="left:888px;top:97px;width:168px;height:125px;background:radial-gradient(circle,#6e2a3a,#d08a4a 45%,#f5f5f5 62%,#fff 100%)"></div>
  <h2 class="section-title" style="left:678px;top:142px">APPETIZERS</h2>

  <div class="item" style="left:679px;top:221px;width:300px"><div class="item__name">Fried Mozzarella Cheese Sticks</div><div class="item__desc">Hand dreaded sticks served with MARINARA SAUCE</div></div>
  <div class="price" style="left:1020px;top:218px">8.99</div>
  <div class="item" style="left:679px;top:260px"><div class="item__name">French Fried Pickles</div><div class="item__desc">BASKET full of Arouse Breaded<br>Pickles with ranch dressing</div></div>
  <div class="price" style="left:1020px;top:257px">8.99</div>
  <div class="item" style="left:679px;top:309px"><div class="item__name">Onion Ring Jower</div></div>
  <div class="price" style="left:1020px;top:306px">8.99</div>
  <div class="item" style="left:679px;top:338px;width:300px"><div class="item__name">Choddan Cheese Jalapeno Poppers</div><div class="item__desc">Fried Cheddan cheese shaffo Jahpenos<br>With ranch dressing (10)</div></div>
  <div class="price" style="left:1020px;top:335px">9.99</div>
  <div class="item" style="left:679px;top:387px"><div class="item__name">Calamari</div><div class="item__desc">Hand Breaded a served with cocktail sause</div></div>
  <div class="price" style="left:1020px;top:384px">12.99</div>
  <div class="item" style="left:679px;top:426px"><div class="item__name">Shaimp Cocktail 1</div><div class="item__desc">10 chilled shrimp with cocktail sause</div></div>
  <div class="price" style="left:1020px;top:423px">11.99</div>
  <div class="item" style="left:679px;top:465px"><div class="item__name">Macho Nachos</div><div class="item__desc">Corn toctilla chips, refreo bams, tomataat,<br>Chili, cheese, salsa, letters, tomato,<br>Jalapeos, &amp; sour cream,</div></div>
  <div class="price" style="left:1020px;top:462px">9.99</div>
  <div class="item" style="left:679px;top:525px"><div class="item__name">Rocky Mountain Oysters</div><div class="item__desc">Full pound at breedeo &amp; Frizo oysters<br>Serves with hosemadoh sause</div></div>
  <div class="price" style="left:1020px;top:522px">12.99</div>

  <div class="photo" role="img" aria-label="Bowl of mixed salad with olives and cheese" style="left:882px;top:576px;width:165px;height:116px;background:radial-gradient(circle,#2f5a22,#c8402e 45%,#f5f5f5 62%,#fff 100%)"></div>
  <h2 class="section-title" style="left:678px;top:624px">Salads</h2>

  <div class="item" style="left:680px;top:702px;width:240px"><div class="item__name">Classic Chef Salad</div><div class="item__desc">Tossed iceburg lettuce, cheesz, tomato,<br>Cucumber, e99, nam, turkey, bacon, croutons,<br>And a garlic broad stick</div></div>
  <div class="price" style="left:1020px;top:699px">9.99</div>
  <div class="item" style="left:680px;top:762px;width:300px"><div class="item__name">Blackeacd Chicken Southwest Salad</div><div class="item__desc">Blackened chickedn served over iceburg lettuce, Cheasz,<br>tomato, sauest corn, black bams, blck olues, Avocados,<br>sour cream, tortilla chips, &amp; southwest dressing.</div></div>
  <div class="price" style="left:1020px;top:759px">9.99</div>
  <div class="item" style="left:680px;top:822px;width:300px"><div class="item__name">West Coast Berry Salad</div><div class="item__desc">Romaine lettuez, black cheasz, E99, tomato,<br>Black &amp; blue berries, strawberries, pineapple, Oranges,<br>almonds, randieo, walnuts, rusbearies, Chicken or sheimp</div></div>
  <div class="price" style="left:1020px;top:819px">9.99</div>
  <div class="item" style="left:680px;top:882px;width:300px"><div class="item__name">Chicken Salad</div><div class="item__desc">Fried or oharbrdiko chicked oven resbury Lettuez,<br>cheese, E99, tomato, cucumberz,<br>bacon Croutons &amp; a garlic bread stick</div></div>
  <div class="price" style="left:1020px;top:879px">9.99</div>
  <div class="item" style="left:680px;top:942px;width:300px"><div class="item__name">Caprese Salad</div><div class="item__desc">Fresh baby spinach, fresh mozzalla, tomato,<br>Calsatmic vinegar, BAS,</div></div>
  <div class="price" style="left:1020px;top:939px">9.99</div>

</div>
</body>
</html>
```